Hero Image Creation for Duchess of Thread (DOT)

Current Site - https://duchessofthread.com.au/
Project: Create 6 high-resolution hero banner images for the Duchess of Thread website to suit the Hero Banner Image of Cartwell
Style: Clean, modern, premium, bright, minimal, white background
1. Marlowe Fabrics Hero Image (Priority #1)
Goal: Showcase Marlowe tana lawn quilting fabrics in a beautiful, premium style. What to include: A mix of Marlowe floral quilting fabrics
Clean white background
Soft, natural lighting
Balanced, aesthetically pleasing composition
Feminine, delicate, elegant feel
Text overlay (must be exactly as below):
H1: Be Inspired to Create
Subheading: Discover Australia's Most Beautiful Range of Marlowe Quilting Fabrics
CTA Button: Shop Marlowe
2–6. Additional Hero Images (to be created after the Marlowe image)
Designers must create banners in a consistent visual style using the same dimensions and white background.
Themes:
Vela Rose Feature Collection
Quilting Fabrics Overview
Fabric Bundles & Curated Packs
Upcycled / Clearance / End-of-Bolt Fabrics
Classes / Creative Community (for 2026)
(Each will have its own text, but the visual brand style must remain cohesive.)
Brand Guidelines:
Clean, premium, modern aesthetic
White, airy background
Pastel tones and floral designs are preferred
Fonts similar to elegant script + clean sans serif (designer may propose alternatives)
Must feel warm, inspiring, and feminine
Avoid clutter — minimalistic but inviting
Deliverables:
6 final hero images in 2048 × 1024 px, highest resolution for Cartwell website
1 editable source file per image (PSD, AI, or layered file)
Ensure text remains readable on desktop and mobile versions
Ensure fabric prints look clear and high-quality
Fabric photos (Marlowe, Vela Rose, etc.)
Brand colours & fonts
# 7 D 8 8 6 E
# A 3 B E A F
# B 4 B 1 C 6
# C 5 A 8 A A
# E B E 5 E2
Bebas Neue Headings
Questrial Body
Overall Objective:
To create a set of visually cohesive hero banners that instantly communicate what Duchess of Thread sells, highlighting:
Marlowe Fabrics
Vela Rose
Bundles
Clearance/upcycled items
Community and classes
The final images must help customers immediately understand what DOT offers and feel inspired to shop.

```html
<!DOCTYPE html>
<html lang="en">
<head>
<meta charset="UTF-8">
<title>Duchess of Thread – Be Inspired to Create</title>
<link href="https://fonts.googleapis.com/css2?family=Bebas+Neue&family=Questrial&display=swap" rel="stylesheet">
<style>
  :root {
    --sage: #7D886E;
    --cream: #F8F6F1;
    --ink: #1E1E1E;
    --white: #FFFFFF;
    --fabric-pink: #EBC9C6;
    --fabric-blue: #D6DCE6;
    --fabric-cream: #F3ECE4;
  }
  * { margin: 0; padding: 0; box-sizing: border-box; }
  html, body {
    width: 1200px;
    height: 600px;
    overflow: hidden;
    background: var(--cream);
  }
  .hero {
    position: relative;
    width: 1200px;
    height: 600px;
    background: var(--cream);
    overflow: hidden;
  }
  .hero-content {
    position: absolute;
    left: 98px;
    top: 146px;
  }
  .hero-title {
    font-family: "Bebas Neue", sans-serif;
    font-weight: 400;
    color: var(--sage);
    font-size: 82px;
    line-height: 70px;
    letter-spacing: 0.5px;
    text-transform: uppercase;
  }
  .hero-subtitle {
    margin-top: 22px;
    font-family: "Questrial", sans-serif;
    color: var(--ink);
    font-size: 19.5px;
    line-height: 31px;
    width: 440px;
  }
  .hero-cta {
    margin-top: 30px;
    display: inline-flex;
    align-items: center;
    gap: 12px;
    height: 52px;
    padding: 0 5px 0 18px;
    border-radius: 26px;
    background: var(--sage);
    color: var(--white);
    font-family: "Questrial", sans-serif;
    font-size: 16px;
    text-decoration: none;
    text-transform: uppercase;
  }
  .hero-cta-icon {
    width: 42px;
    height: 42px;
    border-radius: 50%;
    background: var(--white);
    display: flex;
    align-items: center;
    justify-content: center;
  }
  .hero-fabrics {
    position: absolute;
    left: 690px;
    top: 0;
    width: 480px;
    height: 600px;
  }
</style>
</head>
<body>
  <main class="hero">
    <section class="hero-content">
      <h1 class="hero-title">Be Inspired to<br>Create</h1>
      <p class="hero-subtitle">Discover Australia's Most Beautiful Range of Marlowe Quilting Fabrics</p>
      <a class="hero-cta" href="#">
        Shop Marlowe
        <span class="hero-cta-icon">
          <svg width="20" height="22" viewBox="0 0 20 22" fill="none" stroke="#7D886E" stroke-width="1.6" stroke-linejoin="round">
            <path d="M2 6h16l-1 15H3z"/>
            <path d="M6.5 9V5a3.5 3.5 0 0 1 7 0v4" stroke-linecap="round"/>
          </svg>
        </span>
      </a>
    </section>

    <svg class="hero-fabrics" viewBox="0 0 480 600" role="img" aria-label="Stack of folded pastel floral quilting fabrics in pink, blue, cream and soft yellow">
      <defs>
        <linearGradient id="fabricFloral" x1="0" y1="0" x2="1" y2="1">
          <stop offset="0" stop-color="#F1DDDB"/>
          <stop offset="0.5" stop-color="#EFE6E2"/>
          <stop offset="1" stop-color="#E6E2EA"/>
        </linearGradient>
        <linearGradient id="fabricBlush" x1="0" y1="0" x2="1" y2="0">
          <stop offset="0" stop-color="#E7BDB9"/>
          <stop offset="1" stop-color="#E9C7C3"/>
        </linearGradient>
      </defs>
      <g stroke="rgba(0,0,0,0.06)" stroke-width="1">
        <path d="M146 0 L470 0 L470 28 L460 330 L140 330 Z" fill="url(#fabricFloral)"/>
        <path d="M80 28 L370 70 L360 360 L78 330 Z" fill="url(#fabricBlush)"/>
        <path d="M10 118 L440 150 L430 370 L30 360 Z" fill="url(#fabricFloral)"/>
        <path d="M7 118 L275 106 L280 350 L14 412 Z" fill="url(#fabricFloral)"/>
        <path d="M110 180 L420 160 L430 380 L120 390 Z" fill="url(#fabricFloral)"/>
        <path d="M105 228 L350 240 L356 420 L110 420 Z" fill="url(#fabricFloral)"/>
        <path d="M65 315 L360 300 L372 560 L90 580 Z" fill="url(#fabricFloral)"/>
        <path d="M140 380 L395 408 L390 600 L130 600 Z" fill="url(#fabricFloral)"/>
      </g>
    </svg>
  </main>
</body>
</html>
```